Quillmarsh Property Solutions need a business card design

Hello guys. We would need a business card design asap please.
We are a start up property investment business based in London UK specialised in buying, selling, managing and letting properties and helping distressed property owners.
The name of our Business is Quillmarsh, the logo symbolises the four fundamental elements of the world (earth, air, fire and water) and so it stands for strength, stability, longevity.
We would like the business card to communicate professionalism and reliability. Many many thanks indeed for your work.

Details:

1.) Rosalind Opaleye
Property Investor
Mobile: +44(0)7700361752
Email: rosalind.quillmarsh@brindlepost.co.uk

2.) Anselm Opaleye
Property Investor
Mobile: +44(0)7700584029
Email: anselm.quillmarsh@brindlepost.co.uk

Investment

```html
<!DOCTYPE html>
<html lang="en">
<head>
<meta charset="utf-8">
<title>Quillmarsh Property Solutions – Business Cards</title>
<link rel="stylesheet" href="https://fonts.googleapis.com/css2?family=Josefin+Sans:wght@600;700&family=Quicksand:wght@500;600&display=swap">
<style>
  :root {
    --backdrop: #1c1c1c;
    --red: #d6393b;
    --green: #3e9e4f;
    --blue: #4a78b8;
    --ink: #141414;
    --paper-light: #f3f2f0;
    --paper-dark: #bdb9b5;
    --label-red: #e0262b;
    --label-green: #2fa24a;
    --label-blue: #3d63b0;
  }
  * { margin: 0; padding: 0; box-sizing: border-box; }
  html, body { width: 1200px; height: 900px; overflow: hidden; }
  body {
    position: relative;
    background: var(--backdrop);
    font-family: "Quicksand", sans-serif;
    color: var(--ink);
  }
  .card {
    position: absolute;
    width: 248px;
    height: 383px;
    overflow: hidden;
    text-align: center;
  }
  .card--front { top: 60px; }
  .card--back  { top: 458px; }
  .col-1 { left: 113px; }
  .col-2 { left: 476px; }
  .col-3 { left: 838px; }

  .front-field { position: absolute; inset: 0; }
  .front-field--red   { background: linear-gradient(180deg, var(--red) 0%, #f2d4d2 42%, rgba(255,255,255,0) 44%), linear-gradient(90deg, var(--green) 50%, var(--blue) 50%); }
  .front-field--blue  { background: linear-gradient(180deg, var(--blue) 0%, #d6e0ee 42%, rgba(255,255,255,0) 44%), linear-gradient(90deg, var(--red) 50%, var(--green) 50%); }
  .front-field--green { background: linear-gradient(180deg, var(--green) 0%, #d3ead6 42%, rgba(255,255,255,0) 44%), linear-gradient(90deg, var(--blue) 50%, var(--red) 50%); }

  .brand-dot {
    position: absolute;
    left: 50%;
    transform: translateX(-50%);
    border-radius: 50%;
    background: var(--ink);
  }
  .card--front .brand-dot { top: 196px; width: 26px; height: 26px; }
  .card--back  .brand-dot { top: 138px; width: 18px; height: 18px; }

  .brand-name {
    position: absolute;
    left: 0; right: 0;
    font-family: "Josefin Sans", sans-serif;
    font-weight: 700;
    color: var(--ink);
    letter-spacing: 0.5px;
    line-height: 1;
  }
  .card--front .brand-name { top: 246px; font-size: 27px; }
  .card--back  .brand-name { top: 177px; font-size: 17px; }

  .brand-sub {
    position: absolute;
    left: 0; right: 0;
    font-family: "Josefin Sans", sans-serif;
    font-weight: 700;
    color: var(--ink);
    line-height: 1;
  }
  .card--front .brand-sub { top: 281px; font-size: 14px; }
  .card--back  .brand-sub { top: 199px; font-size: 9px; }

  .card--back {
    background: radial-gradient(ellipse at 50% 40%, var(--paper-light) 0%, #dcdad7 60%, var(--paper-dark) 100%);
  }
  .contact { position: absolute; left: 0; right: 0; top: 246px; }
  .contact__name { font-family: "Josefin Sans", sans-serif; font-weight: 600; font-size: 15px; line-height: 17px; }
  .contact__role { font-size: 11px; line-height: 13px; color: var(--label-red); }
  .contact__label { font-size: 10px; line-height: 11px; margin-top: 12px; }
  .contact__label--mobile { color: var(--label-green); }
  .contact__label--email { color: var(--label-blue); margin-top: 15px; }
  .contact__value { font-size: 14px; line-height: 16px; font-weight: 500; white-space: nowrap; }
  .contact__value--email { font-size: 11.5px; }
</style>
</head>
<body>
  <section class="card card--front col-1">
    <div class="front-field front-field--red" role="img" aria-label="Soft red, green and blue background field"></div>
    <span class="brand-dot"></span>
    <div class="brand-name">QUILLMARSH</div>
    <div class="brand-sub">PROPERTY SOLUTIONS</div>
  </section>
  <section class="card card--front col-2">
    <div class="front-field front-field--blue" role="img" aria-label="Soft blue, red and green background field"></div>
    <span class="brand-dot"></span>
    <div class="brand-name">QUILLMARSH</div>
    <div class="brand-sub">PROPERTY SOLUTIONS</div>
  </section>
  <section class="card card--front col-3">
    <div class="front-field front-field--green" role="img" aria-label="Soft green, blue and red background field"></div>
    <span class="brand-dot"></span>
    <div class="brand-name">QUILLMARSH</div>
    <div class="brand-sub">PROPERTY SOLUTIONS</div>
  </section>

  <section class="card card--back col-1">
    <span class="brand-dot"></span>
    <div class="brand-name">QUILLMARSH</div>
    <div class="brand-sub">PROPERTY SOLUTIONS</div>
    <div class="contact">
      <div class="contact__name">ANSELM OPALEYE</div>
      <div class="contact__role">Property Investor</div>
      <div class="contact__label contact__label--mobile">MOBILE</div>
      <div class="contact__value">+44(0)7700584029</div>
      <div class="contact__label contact__label--email">EMAIL</div>
      <div class="contact__value contact__value--email">anselm.quillmarsh@brindlepost.co.uk</div>
    </div>
  </section>
  <section class="card card--back col-2">
    <span class="brand-dot"></span>
    <div class="brand-name">QUILLMARSH</div>
    <div class="brand-sub">PROPERTY SOLUTIONS</div>
    <div class="contact">
      <div class="contact__name">ROSALIND OPALEYE</div>
      <div class="contact__role">Property Investor</div>
      <div class="contact__label contact__label--mobile">MOBILE</div>
      <div class="contact__value">+44(0)7700361752</div>
      <div class="contact__label contact__label--email">EMAIL</div>
      <div class="contact__value contact__value--email">rosalind.quillmarsh@brindlepost.co.uk</div>
    </div>
  </section>
  <section class="card card--back col-3">
    <span class="brand-dot"></span>
    <div class="brand-name">QUILLMARSH</div>
    <div class="brand-sub">PROPERTY SOLUTIONS</div>
    <div class="contact">
      <div class="contact__name">FUTURE STAFF</div>
      <div class="contact__role">Position</div>
      <div class="contact__label contact__label--mobile">MOBILE</div>
      <div class="contact__value">+XX(0)XXXXXXXXXX</div>
      <div class="contact__label contact__label--email">EMAIL</div>
      <div class="contact__value contact__value--email">futurestaff@brindlepost.co.uk</div>
    </div>
  </section>
</body>
</html>
```